Driving School Business card design

Hi, we are starting a new business (Driving School) and would like your help with our business card design.
We are located in Adelaide SA.
Our aim is to help young people achieve best possible results by promoting safe and stress free driving.

Name of our school is "Velmira" which means best or most favorable.

Hope there is someone out there in wonderful world of design who can think outside of square and give us recognizable/ unique business card design.

Target Market(s)

16+

Industry/Entity Type

Business

Contact Information for Business Card

Name of our business is "Velmira driver training"
Our idea is to make letter "L' in Velmira more distinct (noticeable) by different color or font, so it gets associated with learner driver.
We like combination of white, dark gray and yellow but do not limit our self to that.
Reverse side of our card would have to incorporate writing space for date and time of the next lesson.

Requirements
Must have
• Business name: Velmira driver training
• Owner/ instructor name
• Mobile no:
• Chatterloop logo
Should not have
• Anything Not associated with driving

```html
<!DOCTYPE html>
<html lang="en">
<head>
<meta charset="utf-8">
<title>Velmira Driver Training – Business Card</title>
<link rel="stylesheet" href="https://fonts.googleapis.com/css2?family=Archivo:wght@400;700&display=swap">
<style>
  :root {
    --asphalt-dark: #15181c;
    --asphalt-mid: #23272c;
    --white: #ffffff;
    --line-yellow: #f2c417;
  }
  html, body {
    margin: 0;
    padding: 0;
    width: 1200px;
    height: 762px;
    overflow: hidden;
    background: var(--asphalt-dark);
  }
  .card {
    position: relative;
    width: 1200px;
    height: 762px;
    overflow: hidden;
    font-family: "Archivo", "Helvetica Neue", Arial, sans-serif;
    color: var(--white);
  }
  .card__road {
    position: absolute;
    inset: 0;
    background: radial-gradient(ellipse at 30% 40%, var(--asphalt-mid) 0%, var(--asphalt-dark) 75%);
  }
  .card__lane-lines {
    position: absolute;
    inset: 0;
  }
  .brand {
    position: absolute;
    left: 92px;
    top: 78px;
  }
  .brand__name {
    display: flex;
    align-items: center;
    gap: 18px;
    margin: 0;
    font-weight: 700;
    font-size: 148px;
    line-height: 1;
    letter-spacing: -4px;
    color: var(--white);
  }
  .brand__mark {
    width: 46px;
    height: 46px;
    background: var(--line-yellow);
    margin-top: 40px;
  }
  .brand__tagline {
    margin: 10px 0 0 160px;
    font-weight: 700;
    font-size: 42px;
    letter-spacing: 9px;
    text-transform: uppercase;
    line-height: 1;
  }
  .contact {
    position: absolute;
    left: 88px;
    top: 410px;
  }
  .contact__name {
    margin: 0 0 34px;
    font-weight: 700;
    font-size: 62px;
    letter-spacing: -1px;
    line-height: 1;
  }
  .contact__list {
    margin: 0;
    padding: 0;
    list-style: none;
  }
  .contact__item {
    display: flex;
    align-items: baseline;
    font-size: 38px;
    line-height: 52px;
  }
  .contact__label {
    width: 56px;
    text-align: center;
    font-weight: 700;
  }
  .contact__value {
    font-weight: 400;
  }
</style>
</head>
<body>
  <div class="card">
    <div class="card__road" role="img" aria-label="Photograph of dark asphalt road surface"></div>
    <svg class="card__lane-lines" width="1200" height="762" viewBox="0 0 1200 762" aria-hidden="true">
      <polygon points="730,762 850,762 1200,408 1200,328" fill="var(--line-yellow)"/>
      <polygon points="920,762 1060,762 1200,530 1200,445" fill="var(--line-yellow)"/>
    </svg>

    <header class="brand">
      <h1 class="brand__name">velmira<span class="brand__mark"></span></h1>
      <p class="brand__tagline">Driver Training</p>
    </header>

    <section class="contact">
      <h2 class="contact__name">Liam Harcourt</h2>
      <ul class="contact__list">
        <li class="contact__item"><span class="contact__label">t</span><span class="contact__value">0491570156</span></li>
        <li class="contact__item"><span class="contact__label">f</span><span class="contact__value">velmiradrivertraining</span></li>
        <li class="contact__item"><span class="contact__label">w</span><span class="contact__value">velmiradrivertraining.com.au</span></li>
      </ul>
    </section>
  </div>
</body>
</html>
```